Business Flyer

I want an updated flyer that will have the same content as the one attached but in a different format. They flyers will be passed out to the community and local businesses.

```html
<!DOCTYPE html>
<html lang="en">
<head>
<meta charset="utf-8">
<title>Twirl Juice Bar Flyer</title>
<link href="https://fonts.googleapis.com/css2?family=Roboto+Condensed:wght@300;400&family=Source+Sans+3:wght@400;600&family=Montserrat:wght@600&display=swap" rel="stylesheet">
<style>
  :root {
    --stage: #2a2a2a;
    --paper-light: #fffaf2;
    --paper-edge: #f6d8b0;
    --purple: #7c2c8c;
    --orange: #f0a020;
    --body-ink: #4a4a4a;
    --photo-pink: #eeb1b4;
    --photo-green: #b7c870;
  }
  html, body {
    margin: 0;
    width: 1200px;
    height: 1200px;
    overflow: hidden;
    background: var(--stage);
  }
  .flyer {
    position: absolute;
    left: 205px;
    top: 30px;
    width: 790px;
    height: 1140px;
    background: radial-gradient(ellipse at 50% 45%, var(--paper-light) 35%, var(--paper-edge) 100%);
    font-family: "Roboto Condensed", sans-serif;
    color: var(--purple);
    text-align: center;
  }
  .brand {
    position: absolute;
    top: 70px;
    left: 0;
    right: 0;
    display: flex;
    justify-content: center;
    align-items: center;
    gap: 12px;
    font-size: 34px;
    font-weight: 400;
    letter-spacing: 1px;
  }
  .brand-dot {
    width: 30px;
    height: 30px;
    border-radius: 50%;
    background: var(--orange);
  }
  .headline {
    position: absolute;
    top: 140px;
    left: 20px;
    right: 20px;
    margin: 0;
    font-weight: 400;
    font-size: 66px;
    line-height: 1.02;
    white-space: nowrap;
    text-transform: uppercase;
  }
  .intro {
    position: absolute;
    top: 315px;
    left: 95px;
    right: 95px;
    margin: 0;
    font-family: "Source Sans 3", sans-serif;
    font-size: 16px;
    line-height: 1.4;
    color: var(--body-ink);
  }
  .photo-frame {
    position: absolute;
    top: 460px;
    left: 140px;
    width: 520px;
    height: 340px;
    border: 1.5px solid var(--orange);
  }
  .photo {
    position: absolute;
    top: 500px;
    left: 110px;
    width: 540px;
    height: 340px;
    background: linear-gradient(110deg, #fff 0%, var(--photo-pink) 35%, var(--photo-green) 65%, #fff 100%);
    border-radius: 6px;
  }
  .badge {
    position: absolute;
    top: 500px;
    left: 560px;
    width: 150px;
    height: 150px;
  }
  .badge-text {
    position: absolute;
    top: 542px;
    left: 560px;
    width: 150px;
    font-family: "Montserrat", sans-serif;
    font-weight: 600;
    font-size: 23px;
    line-height: 1.25;
    color: var(--orange);
  }
  .socials {
    position: absolute;
    top: 880px;
    left: 0;
    right: 0;
    display: flex;
    justify-content: center;
    gap: 34px;
    font-size: 23px;
  }
  .social {
    display: flex;
    align-items: center;
    gap: 9px;
  }
  .social-mark {
    width: 22px;
    height: 22px;
    border-radius: 4px;
    background: var(--purple);
  }
  .address {
    position: absolute;
    top: 935px;
    left: 85px;
    right: 85px;
    padding: 18px 0;
    border: 1.5px solid var(--purple);
    font-size: 36px;
    font-weight: 400;
    white-space: nowrap;
  }
</style>
</head>
<body>
  <main class="flyer">
    <div class="brand"><span class="brand-dot"></span><span class="brand-name">TWIRL JUICE BAR</span></div>

    <h1 class="headline">Cold Press Juices &amp;<br>Delicious Smoothies</h1>

    <p class="intro">Thank you for supporting your local business as we aim to provide you with a comfortable and inviting place coupled with great products that is conductive to changing people’s lives and creating a possitive community through our offering of natural cold press juice and delicious smoothies.</p>

    <div class="photo-frame"></div>
    <div class="photo" role="img" aria-label="Photo of strawberry and kiwi smoothies in glasses with straws, surrounded by strawberries, kiwi halves and leaves"></div>

    <svg class="badge" viewBox="0 0 150 150" aria-hidden="true">
      <circle cx="75" cy="75" r="72" fill="var(--paper-light)" stroke="var(--orange)" stroke-width="1.5"/>
      <circle cx="75" cy="75" r="64" fill="none" stroke="var(--orange)" stroke-width="1.5"/>
    </svg>
    <div class="badge-text">100%<br>NATURAL</div>

    <div class="socials">
      <span class="social"><span class="social-mark"></span>Twirl Juice Bar</span>
      <span class="social"><span class="social-mark"></span>TWIRL_JUICE_BAR</span>
    </div>

    <div class="address">4178 Market Lane, Brookfield, MD 20999</div>
  </main>
</body>
</html>
```